Tunnel

a graphic meme to be sent to my clients, consisting of a long angular dark tunnel with a bright light at one end; located within the bright light at the end of the tunnel is the number 2021
the illuminated (shiny silver?) 3 dimensional font message running along the left wall of the tunnel is: BE SAFE.!
the smaller font message underneath the graphic is: Best Wishes For a Healthy New Year
Dan Marlowe Mediator (also to be included nearby is a small semi-circle logo of my corporate logo).

Font styles to use
Sans Serif
Other font styles liked:
• 3 dimensional bold lettering for BE SAFE

```html
<!DOCTYPE html>
<html lang="en">
<head>
<meta charset="utf-8">
<title>Be Safe 2021 – Dan Marlowe Mediator</title>
<link rel="stylesheet" href="https://fonts.googleapis.com/css2?family=Roboto+Condensed:wght@400;700;900&display=swap">
<style>
  :root {
    --ink: #000000;
    --light: #ffffff;
    --steel: #6c6c6c;
    --steel-side: #242424;
    --steel-deep: #141414;
    --year: #1c1b2c;
    --text: #ececec;
    --badge: #1f1b4a;
  }
  html, body {
    margin: 0;
    padding: 0;
    width: 1200px;
    height: 1200px;
    overflow: hidden;
    background: var(--ink);
  }
  .card {
    position: relative;
    width: 1200px;
    height: 1200px;
    overflow: hidden;
    font-family: "Roboto Condensed", "Arial Narrow", sans-serif;
    background: var(--ink);
  }
  .tunnel-scene {
    position: absolute;
    inset: 0;
    background:
      radial-gradient(ellipse 300px 260px at 610px 380px, rgba(235,235,235,0.55) 0%, rgba(120,120,120,0.25) 45%, rgba(0,0,0,0) 100%),
      radial-gradient(ellipse 460px 420px at 610px 600px, rgba(80,80,80,0.45) 0%, rgba(25,25,25,0.25) 55%, rgba(0,0,0,0) 100%),
      radial-gradient(ellipse 600px 440px at 640px 320px, rgba(55,55,55,0.6) 0%, rgba(0,0,0,0) 100%),
      var(--ink);
  }
  .tunnel-light {
    position: absolute;
    left: 505px;
    top: 215px;
    width: 215px;
    height: 215px;
    border-radius: 110px 110px 6px 6px;
    background: radial-gradient(ellipse at 50% 55%, var(--light) 0%, var(--light) 55%, #e6e6e6 100%);
    filter: blur(6px);
  }
  .wall-message {
    margin: 0;
    font-weight: 900;
  }
  .wall-word {
    position: absolute;
    display: block;
    line-height: 1;
    white-space: nowrap;
    color: var(--steel);
    transform-origin: left center;
    text-shadow:
      -2px 1px 0 var(--steel-side), -4px 2px 0 var(--steel-side), -6px 3px 0 var(--steel-side),
      -8px 4px 0 var(--steel-side), -10px 5px 0 var(--steel-side), -12px 6px 0 var(--steel-deep),
      -14px 7px 0 var(--steel-deep), -16px 8px 0 var(--steel-deep),
      0 0 22px rgba(255,255,255,0.22);
  }
  .word-be {
    left: 80px;
    top: 58px;
    font-size: 520px;
    transform: perspective(900px) rotateY(35deg) scaleX(0.62);
  }
  .word-safe {
    left: 350px;
    top: 172px;
    font-size: 320px;
    color: #7a7a7a;
    transform: perspective(700px) rotateY(35deg) scaleX(0.3);
  }
  .year {
    position: absolute;
    left: 542px;
    top: 296px;
    margin: 0;
    font-size: 96px;
    font-weight: 700;
    line-height: 1;
    letter-spacing: -1px;
    color: var(--year);
    transform: scaleX(0.8);
    transform-origin: left center;
    text-shadow: 0 0 3px rgba(255,255,255,0.9), 0 0 1px #fff;
  }
  .greeting {
    position: absolute;
    left: 0;
    width: 1212px;
    top: 735px;
    margin: 0;
    text-align: center;
    font-size: 76px;
    font-weight: 700;
    color: var(--text);
    line-height: 1;
    -webkit-text-stroke: 5px #000;
    paint-order: stroke fill;
    text-shadow: 0 0 14px rgba(255,255,255,0.55);
  }
  .signature {
    position: absolute;
    left: 0;
    width: 1240px;
    top: 890px;
    margin: 0;
    text-align: center;
    font-size: 55px;
    font-weight: 400;
    color: var(--text);
    line-height: 1;
  }
  .firm {
    position: absolute;
    left: 0;
    width: 1230px;
    top: 1045px;
    display: flex;
    justify-content: center;
    align-items: center;
    gap: 16px;
  }
  .firm-dot {
    width: 34px;
    height: 34px;
    border-radius: 50%;
    background: var(--badge);
  }
  .firm-name {
    font-size: 40px;
    font-weight: 400;
    color: var(--text);
    line-height: 1;
  }
</style>
</head>
<body>
  <main class="card">
    <div class="tunnel-scene" role="img" aria-label="Long dark brick railway tunnel receding toward a bright opening">
      <div class="tunnel-light"></div>
    </div>

    <h1 class="wall-message" aria-label="Be safe!">
      <span class="wall-word word-be">BE</span>
      <span class="wall-word word-safe">SAFE!</span>
    </h1>

    <p class="year">2021</p>

    <h2 class="greeting">Best Wishes For a Healthy New Year</h2>

    <p class="signature">Dan Marlowe Mediator</p>

    <div class="firm">
      <span class="firm-dot"></span>
      <span class="firm-name">Harlow Bennett Reyes</span>
    </div>
  </main>
</body>
</html>
```